Briefpapier und Visitenkarten
Zielgruppe
Das Design soll Herren im mittleren bis hohen Alter ansprechen.
Aufgabenstellung
Benötigt wird ein Briefpapier für die Koresspondenz und die Rechnungen. Ein Logo ist vorhanden und muss ins Briefpapier und auf die Visitenkarten einbebunden werden.

```html
<!DOCTYPE html>
<html lang="de">
<head>
<meta charset="utf-8">
<title>Briefpapier – nordtal it partner</title>
<link rel="stylesheet" href="https://fonts.googleapis.com/css2?family=Arimo:wght@400;700&display=swap">
<style>
  :root {
    --brand-red: #d3122f;
    --ink: #1c1c1c;
    --logo-grey: #3a3a3a;
    --paper: #ffffff;
    --footer-bg: #f2f2f2;
  }
  * { margin: 0; padding: 0; box-sizing: border-box; }
  html, body { width: 900px; height: 1200px; overflow: hidden; background: var(--paper); }
  .letterhead {
    position: relative;
    width: 900px;
    height: 1200px;
    background: var(--paper);
    font-family: "Arimo", Arial, sans-serif;
    color: var(--ink);
    overflow: hidden;
  }
  .side-bar {
    position: absolute;
    top: 0; right: 0;
    width: 18px; height: 100%;
    background: var(--brand-red);
  }
  .brand {
    position: absolute;
    left: 92px; top: 104px;
    display: flex; align-items: center; gap: 12px;
  }
  .brand-dot {
    width: 22px; height: 22px;
    border-radius: 50%;
    background: var(--brand-red);
  }
  .brand-name {
    font-size: 34px;
    font-weight: 400;
    color: var(--logo-grey);
    letter-spacing: 0.5px;
  }
  .sender-line {
    position: absolute;
    left: 128px; top: 200px;
    font-size: 11px;
    font-weight: 700;
  }
  .footer {
    position: absolute;
    left: 0; right: 18px; bottom: 0;
    height: 124px;
    background: var(--footer-bg);
    border-top: 2px solid var(--brand-red);
    text-align: center;
    padding-top: 28px;
  }
  .footer-name {
    font-size: 15px;
    font-weight: 700;
  }
  .footer-name .contact-person { color: var(--brand-red); }
  .footer-address {
    margin-top: 10px;
    font-size: 13px;
    font-weight: 700;
  }
  .footer-address .sep { color: var(--brand-red); font-weight: 400; }
</style>
</head>
<body>
  <main class="letterhead">
    <div class="side-bar"></div>

    <header class="brand">
      <span class="brand-dot"></span>
      <span class="brand-name">nordtal it partner</span>
    </header>
    <p class="sender-line">Lindenweg 12 | 42101 Musterstadt</p>

    <footer class="footer">
      <p class="footer-name">nordtal it partner &nbsp;<span class="contact-person">| Jonas Beispiel</span></p>
      <p class="footer-address">Lindenweg 12 | 42101 Musterstadt <span class="sep">|</span> Telefon 0 21 00 - 5 40 12 <span class="sep">|</span> Fax 0 21 00 - 5 40 13</p>
    </footer>
  </main>
</body>
</html>
```